Harbor Lanterns: Walking Beside Young Ones Through Every Season

This book is about being a good father and how to parent them well so they are fully equipped to launch into the world when they become adults. It is an encouraging and practical guide that acknowledges the difficulties of being a good father and provides strategies for addressing them.

Target Market(s)

My target market is dads, or people that will gift this book to a dad that they know

```html
<!DOCTYPE html>
<html lang="en">
<head>
<meta charset="utf-8">
<title>Harbor Lanterns — Book Cover</title>
<link href="https://fonts.googleapis.com/css2?family=Anton&family=Montserrat:wght@400&display=swap" rel="stylesheet">
<style>
  :root {
    --page: #ffffff;
    --sky-top: #a88c68;
    --sky-mid: #dcae6c;
    --sky-warm: #f3a846;
    --sky-low: #d9772f;
    --shore: #3a2212;
    --sun: #fff6d8;
    --gold: #fdd66e;
    --rule: #f1cd6c;
    --ink: #0b0b0b;
    --sub: #2e2a26;
  }
  html, body {
    margin: 0;
    padding: 0;
    width: 1200px;
    height: 1200px;
    overflow: hidden;
    background: var(--page);
  }
  .cover {
    position: relative;
    width: 1200px;
    height: 1200px;
    background: var(--page);
  }
  .cover-photo {
    position: absolute;
    left: 65px;
    top: 65px;
    width: 1070px;
    height: 1070px;
    background:
      radial-gradient(circle at 87% 64%, var(--sun) 0, rgba(255,236,170,0.85) 3%, rgba(255,200,100,0.45) 16%, rgba(255,180,80,0) 34%),
      linear-gradient(180deg, var(--sky-top) 0%, var(--sky-mid) 42%, var(--sky-warm) 68%, var(--sky-low) 82%, var(--shore) 100%);
  }
  .title-frame {
    position: absolute;
    left: 400px;
    top: 105px;
    width: 573px;
    height: 333px;
  }
  .title {
    position: absolute;
    left: 422px;
    top: 112px;
    margin: 0;
    font-family: 'Anton', sans-serif;
    font-weight: 400;
    font-size: 174px;
    line-height: 152px;
    text-transform: uppercase;
    letter-spacing: 1px;
  }
  .title-line { display: block; }
  .title-line--gold { color: var(--gold); }
  .title-line--dark { color: var(--ink); }
  .subtitle {
    position: absolute;
    right: 226px;
    top: 468px;
    margin: 0;
    font-family: 'Montserrat', sans-serif;
    font-weight: 400;
    font-size: 30px;
    line-height: 35px;
    letter-spacing: 1px;
    text-align: right;
    color: var(--sub);
  }
</style>
</head>
<body>
  <div class="cover">
    <div class="cover-photo" role="img" aria-label="Sunset photograph: silhouette of a father holding hands with two young children beside a lake, hills and shrubs against a golden sky"></div>

    <svg class="title-frame" viewBox="0 0 573 333" aria-hidden="true">
      <polyline points="228,1 1,1 1,332 573,332" fill="none" stroke="var(--rule)" stroke-width="2"/>
    </svg>

    <h1 class="title">
      <span class="title-line title-line--gold">Harbor</span>
      <span class="title-line title-line--dark">Lanterns</span>
    </h1>

    <p class="subtitle">Walking Beside Young Ones<br>Through Every Season</p>
  </div>
</body>
</html>
```